Marrowgate Gemworks Website revamp

Hi,

We need a working WordPress theme, not just a .PSD file. Thank you.

We need a complete revamp of our website. We sell lab grown diamonds online. We sell the idea that everyone should be able to afford a diamond. Thus our diamonds are priced very reasonably. Our selling point "the joy of giving and receiving a diamond in a little box".

Our range of products includes rings, bangles, necklace, ear rings etc. We currently only operate in Singapore. Some photos of our products are on our websites.

Need.
- Clean look and feel, simplistic preferably white and soft colours
- Easy to navigate
- No banners
- E Com
- Introduction page
- Willing to change logo if needed

Existing page: www.marrowgategemworks.com

Target Market(s)

Young ladies
Ladies
Men buying for ladies
Young boyfriends fresh out of school buying for love ones
Working ladies to match what they wear to work

Industry/Entity Type

Online

Requirements
Must have
• ECOM. Product shopping cart
Pictures uploads
Intro page
Nice to have
• Pastel colors preferred. - Color scheme is important in our business to create a long term impression. Color scheme will also be used for next potential project, i.e. packaging design.

Should not have
• Should not have old style fonts.

```html
<!DOCTYPE html>
<html lang="en">
<head>
<meta charset="utf-8">
<title>Marrowgate Gemworks</title>
<link href="https://fonts.googleapis.com/css2?family=Source+Sans+3:wght@400;600&display=swap" rel="stylesheet">
<style>
:root{
  --sky:#a9d8f2;
  --sky-deep:#7cc3ea;
  --nav-text:#3d84b5;
  --heading-blue:#4b9cc9;
  --lilac:#9a74b6;
  --lilac-link:#b06fb8;
  --text:#555;
  --muted:#777;
  --line:#dcdcdc;
  --band:#f2f2f2;
  --footer:#2d2d2d;
  --footer-text:#bdbdbd;
}
*{margin:0;padding:0;box-sizing:border-box}
html,body{width:1200px;height:1138px;overflow:hidden;background:#fff}
body{font-family:"Source Sans 3",sans-serif;color:var(--text)}
.page{position:relative;width:1200px;height:1138px;overflow:hidden}
.abs{position:absolute}

.masthead{left:0;top:0;width:1200px;height:198px;background:linear-gradient(#fafafa,#f0f0f0);border-bottom:1px solid #e4e4e4}
.brand{left:0;width:1200px;top:70px;text-align:center;font-size:32px;font-weight:400;color:#7a6c5a;letter-spacing:.5px}
.brand-dot{display:inline-block;width:14px;height:14px;border:2px solid #7a6c5a;margin-right:12px;vertical-align:middle}

.ribbon{top:179px;width:48px;height:38px;background:var(--sky-deep)}
.ribbon.left{left:55px;clip-path:polygon(0 0,100% 0,100% 100%,0 100%,40% 50%)}
.ribbon.right{left:1097px;clip-path:polygon(0 0,100% 0,60% 50%,100% 100%,0 100%)}
.mainnav{left:99px;top:173px;width:1002px;height:48px;background:linear-gradient(#bfe3f7,#9fd3f0);border:1px solid var(--sky-deep);border-radius:3px;box-shadow:0 1px 3px rgba(0,0,0,.15)}
.mainnav ul{list-style:none}
.mainnav li{position:absolute;top:13px;font-size:15px;color:var(--nav-text);white-space:nowrap}
.mainnav li.current{color:#1f4e6e;font-weight:600}
.cart{left:806px;top:5px;width:190px;height:36px;background:#fff;border-radius:3px;font-size:14px;color:var(--muted);padding:8px 0 0 38px;white-space:nowrap}
.cart b{color:#8a6d3b;font-weight:600}
.cart svg{position:absolute;left:10px;top:10px}

.slider{left:99px;top:235px;width:1002px;height:384px;border:1px solid var(--line);background:#f4f4f6;overflow:hidden}
.slide-photo{left:0;top:0;width:592px;height:384px;background:radial-gradient(ellipse 140px 100px at 60px 60px,#4a3f47 0%,#8e8589 45%,rgba(230,228,232,0) 100%),radial-gradient(ellipse 260px 160px at 180px 300px,#c6c3cc 0%,rgba(236,235,238,0) 100%),radial-gradient(ellipse 150px 170px at 440px 200px,#d9d8dc 0%,rgba(240,240,242,0) 100%),linear-gradient(100deg,#e4e2e5 0%,#efeef1 55%,#f4f4f6 100%)}
.slide-title{right:44px;top:74px;text-align:right;color:var(--lilac);font-size:38px;line-height:1;font-weight:400}
.slide-sub{right:44px;top:114px;text-align:right;color:var(--lilac);font-size:27px;font-weight:400}
.slide-copy{right:44px;top:158px;text-align:right;font-size:17px;line-height:25px;color:#666}
.btn-more{left:859px;top:224px;width:95px;height:32px;border:1px solid #c28fc6;border-radius:3px;background:linear-gradient(#e6c2e7,#cf9ed2);color:#5a3a63;font-size:14px;text-align:center;line-height:30px}
.dots{left:893px;top:345px}
.dots span{display:inline-block;width:14px;height:14px;border-radius:50%;background:#c4c4c8;margin-right:9px;box-shadow:inset 0 1px 2px rgba(0,0,0,.25)}
.dots span.on{background:#8b8b90}

.col-title{top:655px;font-size:21px;color:var(--heading-blue);font-weight:400}
.col-arrow{top:658px;width:19px;height:19px;border-radius:50%;background:#e6e6e6;border:1px solid #d0d0d0}
.col-arrow::after{content:"";position:absolute;left:7px;top:5px;border-left:5px solid #666;border-top:4px solid transparent;border-bottom:4px solid transparent}
.card{top:689px;width:311px;height:156px;border:1px solid var(--line);background:#fff}
.card .thumb{position:absolute;left:16px;top:22px;width:100px;height:110px;border-radius:4px}
.card .divider{position:absolute;left:155px;top:10px;width:1px;height:134px;background:#eee}
.about-copy{left:129px;top:16px;width:178px;font-size:13px;line-height:20.5px;color:#555;letter-spacing:-.1px}
.about-more{left:129px;top:121px;font-size:13px;color:var(--lilac-link)}
.prod-name{left:179px;top:31px;font-size:19px;color:var(--heading-blue)}
.prod-price{left:179px;top:58px;font-size:16px;color:var(--lilac)}
.btn-cart{left:179px;top:92px;width:85px;height:27px;border-radius:3px;background:linear-gradient(#bdbdbd,#9a9a9a);color:#333;font-size:14px;line-height:27px;text-align:center}

.cat{top:867px;width:228px;height:41px;background:linear-gradient(#f3f3f3,#e6e6e6);border:1px solid #d6d6d6;font-size:19px;color:#777;line-height:39px}
.cat i{position:absolute;top:11px;width:1px;height:17px;background:#ccc}
.cat svg{position:absolute;top:14px}

.infoband{left:0;top:940px;width:1200px;height:96px;background:var(--band)}
.info{font-size:14px;color:#666;line-height:23px;white-space:nowrap}
.footer{left:0;top:1036px;width:1200px;height:102px;background:var(--footer)}
.footlinks{left:101px;top:23px;font-size:14px;color:var(--footer-text)}
.footlinks span.sep{margin:0 10px;color:#888}
.copyright{left:101px;top:58px;font-size:14px;color:var(--footer-text)}
.social{top:38px;width:25px;height:25px;border-radius:50%;background:#6f6f6f}
</style>
</head>
<body>
<div class="page">

  <header class="abs masthead">
    <div class="abs brand"><span class="brand-dot"></span>Marrowgate Gemworks</div>
  </header>

  <div class="abs ribbon left"></div>
  <div class="abs ribbon right"></div>
  <nav class="abs mainnav">
    <ul>
    <li class="current" style="left:28px">HOME</li>
    <li style="left:105px">ABOUT US</li>
    <li style="left:210px">OUR DIAMONDS</li>
    <li style="left:354px">OUR SHOP</li>
    <li style="left:461px">MY ACCOUNT</li>
    <li style="left:588px">MY CART</li>
    <li style="left:684px">CHECK OUT</li>
    </ul>
    <div class="abs cart">
      <svg width="20" height="16" viewBox="0 0 20 16"><path d="M1 2h3l2 9h10l2-6H6" fill="none" stroke="#a08a66" stroke-width="1.4"/><circle cx="8" cy="14" r="1.4" fill="#a08a66"/><circle cx="15" cy="14" r="1.4" fill="#a08a66"/></svg>
      <b>0</b> item(s) &nbsp;/&nbsp; Total : <b>$0.00</b>
    </div>
  </nav>

  <section class="abs slider">
    <div class="abs slide-photo" role="img" aria-label="Photo of diamond-set eternity rings and hoop earrings on a soft white surface beside a dark stone"></div>
    <h1 class="abs slide-title">WELCOME TO</h1>
    <h2 class="abs slide-sub">MARROWGATE GEMWORKS</h2>
    <p class="abs slide-copy">Diamonds bear the toll of heat and pressure<br>to be formed. A gift of a ...</p>
    <div class="abs btn-more">Know more</div>
    <div class="abs dots"><span class="on"></span><span></span><span></span><span></span></div>
  </section>

  <h3 class="abs col-title" style="left:111px">ABOUT MARROWGATE</h3>
  <div class="abs card" style="left:111px">
    <div class="thumb" role="img" aria-label="Turquoise gift box tied with a white ribbon" style="background:linear-gradient(#8fdcd6,#3fbdb3)"></div>
    <p class="abs about-copy">When Tomas met Elena, Tomas was a poor bloke. Just out of school, embarking on his first job and without a stable pay. Tomas wanted to buy...</p>
    <a class="abs about-more">More</a>
  </div>

  <h3 class="abs col-title" style="left:444px">DIAMONDS</h3>
  <div class="abs col-arrow" style="left:734px"></div>
  <div class="abs card" style="left:445px">
    <div class="thumb" role="img" aria-label="Pair of diamond drop earrings" style="background:linear-gradient(#f4f4f4,#dcdcdc)"></div>
    <div class="divider"></div>
    <div class="abs prod-name">DROP</div>
    <div class="abs prod-price">Price : $500</div>
    <div class="abs btn-cart">Add to Cart</div>
  </div>

  <h3 class="abs col-title" style="left:778px">FEATURED PRODUCT</h3>
  <div class="abs col-arrow" style="left:1063px"></div>
  <div class="abs card" style="left:779px">
    <div class="thumb" role="img" aria-label="Silver ring with a pink centre stone" style="background:linear-gradient(#e9dcef,#cfcfd4)"></div>
    <div class="divider"></div>
    <div class="abs prod-name">RING</div>
    <div class="abs prod-price">Price : $500</div>
    <div class="abs btn-cart">Add to Cart</div>
  </div>

  <div class="abs cat" style="left:110px"><svg width="6" height="10" viewBox="0 0 6 10" style="left:60px"><path d="M1 1l4 4-4 4" fill="none" stroke="#888" stroke-width="1.3"/></svg><i style="left:72px"></i><span style="padding-left:82px">BANGLES</span></div>
  <div class="abs cat" style="left:360px"><svg width="6" height="10" viewBox="0 0 6 10" style="left:59px"><path d="M1 1l4 4-4 4" fill="none" stroke="#888" stroke-width="1.3"/></svg><i style="left:71px"></i><span style="padding-left:82px">BRACELETS</span></div>
  <div class="abs cat" style="left:612px"><svg width="6" height="10" viewBox="0 0 6 10" style="left:59px"><path d="M1 1l4 4-4 4" fill="none" stroke="#888" stroke-width="1.3"/></svg><i style="left:71px"></i><span style="padding-left:82px">EARRINGS</span></div>
  <div class="abs cat" style="left:862px"><svg width="6" height="10" viewBox="0 0 6 10" style="left:74px"><path d="M1 1l4 4-4 4" fill="none" stroke="#888" stroke-width="1.3"/></svg><i style="left:86px"></i><span style="padding-left:96px">RINGS</span></div>

  <section class="abs infoband">
    <svg class="abs" style="left:131px;top:36px" width="24" height="26" viewBox="0 0 24 26"><rect x="1" y="3" width="22" height="22" fill="#8d8d8d"/><rect x="5" y="0" width="8" height="14" fill="#f2f2f2"/><rect x="7" y="0" width="4" height="11" fill="#8d8d8d"/></svg>
    <div class="abs info" style="left:168px;top:25px">27 Fernvale Crescent, #03-B4<br>Linden Court Mall, Singapore 540012</div>
    <svg class="abs" style="left:509px;top:35px" width="30" height="28" viewBox="0 0 30 28"><path d="M4 4c3-3 6-2 7 0l-3 4c3 6 8 11 14 13l3-3c2 1 4 4 1 7-6 4-24-11-22-21z" fill="#8d8d8d"/></svg>
    <div class="abs info" style="left:550px;top:36px">Phone : &nbsp;+65 9000 4172</div>
    <svg class="abs" style="left:788px;top:40px" width="27" height="19" viewBox="0 0 27 19"><rect width="27" height="19" fill="#8d8d8d"/><path d="M0 0l13.5 10L27 0" fill="none" stroke="#f2f2f2" stroke-width="1.5"/></svg>
    <div class="abs info" style="left:827px;top:37px">E-mail : info@marrowgategemworks.com</div>
  </section>

  <footer class="abs footer">
    <div class="abs footlinks">Home<span class="sep">|</span>About us<span class="sep">|</span>Our Diamonds<span class="sep">|</span>Our Shop<span class="sep">|</span>My Account<span class="sep">|</span>My Cart<span class="sep">|</span>Check out<span class="sep">|</span>Contact us</div>
    <div class="abs copyright">Copyright &nbsp;©&nbsp; 2013 &nbsp;Marrowgate. &nbsp;All rights reserved.</div>
    <div class="abs social" style="left:970px"></div>
    <div class="abs social" style="left:1005px"></div>
    <div class="abs social" style="left:1040px"></div>
    <div class="abs social" style="left:1075px"></div>
  </footer>

</div>
</body>
</html>
```